I need a better looking dashboard for my web application

I have a very table heavy web page that I would like to add a design touch to it. I have the logo and primary colors picked out, I just need some help in adding visual appeal the page. I would also like to add a couple of button to the page as shortcuts. Every spot that has a + sign could have a button added. I would also like to add another graph (the data will be in the uploaded files. Please feel free to ask any questions :-)

```html
<!DOCTYPE html>
<html lang="en">
<head>
<meta charset="utf-8">
<title>CoverDesk – Sub Management Dashboard</title>
<link href="https://fonts.googleapis.com/css2?family=Poppins:wght@500;600;700&family=Montserrat:wght@500;600;700&family=Inter:wght@400;500&display=swap" rel="stylesheet">
<style>
  :root{
    --cyan:#8ee6ee;
    --cyan-soft:#a6eef3;
    --lilac:#c19bd0;
    --white:#ffffff;
    --ink:#111111;
    --line:#cfd3e6;
    --violet:#6d4fb8;
    --violet-tab:#c4a4f5;
    --indigo:#3a2cc8;
    --purple-mid:#6c5ce7;
    --purple-light:#9b8cf8;
    --blue:#437bd8;
    --bar-purple:#5f3596;
    --bar-red:#dd3445;
    --bar-green:#2fae4a;
    --teal:#27a9cf;
    --link:#1f5fe0;
    --card-border:#d9c9f2;
  }
  *{box-sizing:border-box;margin:0;padding:0}
  html,body{width:1200px;height:1200px;overflow:hidden;background:var(--white)}
  body{position:relative;font-family:"Inter",sans-serif;color:var(--ink)}
  .abs{position:absolute}

  .panel{position:absolute;left:96px;top:231px;width:1015px;height:745px;border-radius:36px;overflow:hidden;
    background:linear-gradient(90deg,var(--lilac) 0%,#b6b3da 50%,var(--cyan-soft) 100%)}
  .panel::before{content:"";position:absolute;inset:0;
    background:linear-gradient(90deg,var(--cyan) 0%,#b0b8dd 55%,var(--lilac) 100%);
    -webkit-mask-image:linear-gradient(180deg,#000 0%,#000 30%,transparent 80%);
    mask-image:linear-gradient(180deg,#000 0%,#000 30%,transparent 80%)}

  .brand{left:139px;top:247px;font-family:"Montserrat",sans-serif;font-weight:600;font-size:27px;color:var(--violet);letter-spacing:.2px}
  .section-title{left:139px;top:292px;font-family:"Montserrat",sans-serif;font-size:13px;letter-spacing:2.2px;font-weight:500}
  .view-switch{left:139px;top:311px;height:21px;display:flex;border-radius:4px;overflow:hidden;font-size:6.5px}
  .view-switch span{display:flex;align-items:center;justify-content:center;width:48px;background:#eceaf0;color:#222}
  .view-switch .active{background:var(--violet-tab);color:#fff;width:48px}
  .view-switch span+span{width:52px}

  .topnav{left:521px;top:246px;width:251px;height:32px;background:#fff;border-radius:3px 0 0 3px;display:flex;align-items:center;gap:11px;padding-left:14px;font-size:10px;white-space:nowrap;overflow:hidden}
  .topnav .item{display:flex;align-items:center;gap:4px}
  .menu-open{left:772px;top:246px;width:118px;height:76px;border-radius:3px 3px 8px 8px;overflow:hidden;background:#fff}
  .menu-open .head{height:32px;background:var(--violet-tab);display:flex;align-items:center;gap:6px;padding-left:8px;font-size:10.5px;color:#1b1b40;white-space:nowrap}
  .menu-open .opt{display:flex;align-items:center;gap:6px;padding-left:10px;font-size:8.5px;height:19px;white-space:nowrap}
  .menu-open .opt:first-of-type{margin-top:3px}
  .user-pill{left:904px;top:246px;width:162px;height:32px;background:var(--violet-tab);border-radius:3px;display:flex;align-items:center;gap:5px;padding-left:13px;font-size:9px;color:#1b1b40;white-space:nowrap}

  .card{position:absolute;background:#fff;border-radius:12px;border:1.5px solid var(--card-border)}
  .h-card{font-family:"Poppins",sans-serif;font-weight:700;color:var(--ink)}

  .summary{left:140px;top:339px;width:511px;height:84px}
  .summary h2{position:absolute;left:9px;top:7px;font-size:18px}
  .legend{position:absolute;left:10px;top:33px;display:flex;gap:5px;font-size:8.2px;align-items:center}
  .legend i{display:inline-block;width:6px;height:6px;border-radius:50%;margin-right:3px;vertical-align:middle}
  .summary .date{position:absolute;left:9px;top:57px;font-size:8.2px}
  .stack{position:absolute;left:47px;top:56px;width:444px;height:18px;display:flex}

  .overview{left:142px;top:441px;width:323px;height:220px}
  .overview h2{position:absolute;left:19px;top:6px;font-family:"Montserrat",sans-serif;font-weight:700;font-size:15px;letter-spacing:1.2px}
  .overview .sub{position:absolute;left:0;right:0;top:33px;text-align:center;font-size:7.6px}

  .fill{left:483px;top:441px;width:168px;height:220px}
  .fill h2{position:absolute;left:14px;top:11px;font-family:"Montserrat",sans-serif;font-weight:700;font-size:13.5px;letter-spacing:1px;white-space:nowrap}
  .dlabel{position:absolute;font-size:7.8px;line-height:11px}

  .profiles{left:671px;top:338px;width:393px;height:323px}
  .profiles h2{position:absolute;left:0;right:0;top:20px;text-align:center;font-size:17px}
  .t-small{position:absolute;font-size:8.2px;white-space:nowrap}
  .rule{position:absolute;height:1px;background:var(--line)}
  .photo{position:absolute;width:28px;height:29px;border-radius:3px}
  .none{color:var(--link);font-size:7.8px}

  .tabs{top:686px;font-family:"Poppins",sans-serif;font-weight:700;font-size:12px;white-space:nowrap}
  .tab-line{left:251px;top:705px;width:60px;height:2px;background:var(--teal);border-radius:1px}

  .requests{left:142px;top:714px;width:697px;height:240px;border-color:#eae3f7}
  .col-head{position:absolute;font-family:"Montserrat",sans-serif;font-weight:500;white-space:nowrap}
  .col-head.big{font-size:14px;letter-spacing:1.8px}
  .col-head.small{font-size:7.5px;letter-spacing:1.3px}
  .cell{position:absolute;font-size:7.8px;white-space:nowrap;line-height:12px}
  .avatar{position:absolute;width:8px;height:9px;border-radius:1px}
  .initials{position:absolute;width:9px;height:9px;border-radius:2px;background:var(--teal);color:#fff;font-size:5px;font-weight:500;display:flex;align-items:center;justify-content:center}
  .scroll{left:828px;top:843px;width:2px;height:51px;background:var(--teal);border-radius:1px}

  .monthly{left:856px;top:714px;width:209px;height:144px}
  .monthly h2{position:absolute;left:0;right:0;top:11px;text-align:center;font-family:"Montserrat",sans-serif;font-weight:700;font-size:15px;letter-spacing:1.2px}
  .stat{position:absolute;font-size:9.5px;letter-spacing:1.4px;font-family:"Montserrat",sans-serif;font-weight:500}

  .btn{position:absolute;height:29px;border-radius:3px;display:flex;align-items:center;justify-content:center;font-family:"Montserrat",sans-serif;font-weight:700;font-size:10px;letter-spacing:1px;background:#fff;color:var(--ink);white-space:nowrap}
  .btn.primary{background:var(--violet);color:#fff}
</style>
</head>
<body>
  <div class="panel"></div>

  <div class="abs brand">CoverDesk</div>
  <div class="abs section-title">Sub Management</div>
  <div class="abs view-switch"><span class="active">Dashboard</span><span>Calendar</span></div>

  <nav class="abs topnav">
    <span class="item"><svg width="11" height="11" viewBox="0 0 12 12" fill="none" stroke="#222" stroke-width="1"><path d="M1.5 6 6 2l4.5 4M3 5v5.5h2.2V8h1.6v2.5H9V5"/></svg>Home</span>
    <span class="item"><svg width="10" height="11" viewBox="0 0 11 12"><path d="M5.5 1C6 3.5 9.5 5 9.5 8a4 4 0 0 1-8 0C1.5 6 3 5 3.5 3.5 4.3 5 5 5 5 5 5 3.5 5.2 2.3 5.5 1z" fill="#222"/></svg>Demo Outbox</span>
    <span class="item">Location Admin</span>
  </nav>
  <div class="abs menu-open">
    <div class="head"><svg width="11" height="9" viewBox="0 0 12 10" fill="none" stroke="#333" stroke-width=".9"><circle cx="4" cy="3" r="1.8"/><circle cx="8.5" cy="3" r="1.5"/><path d="M1 9c0-2 1.4-3 3-3s3 1 3 3M7 6.3c2 0 3.5.8 3.5 2.7"/></svg>Regular Staff<svg width="8" height="6" viewBox="0 0 9 6" style="margin-left:4px"><path d="M1 1l3.5 3.5L8 1" fill="none" stroke="#555" stroke-width=".9"/></svg></div>
    <div class="opt"><svg width="8" height="8" viewBox="0 0 8 8"><path d="M1 7l1-3 4-3 1 1-3 4z" fill="#222"/></svg>Manage Regular Staff</div>
    <div class="opt"><svg width="9" height="8" viewBox="0 0 9 8" fill="none" stroke="#222" stroke-width=".8"><rect x=".5" y="1.2" width="8" height="6.3"/><path d="M.5 3h8M2.5 0v2M6.5 0v2"/></svg>Leave Requests</div>
  </div>
  <div class="abs user-pill"><svg width="11" height="9" viewBox="0 0 11 9"><circle cx="4" cy="2.5" r="2" fill="#222"/><circle cx="8" cy="3" r="1.6" fill="#222"/><path d="M0 9c0-2.5 1.8-3.6 4-3.6S8 6.5 8 9zM8.5 5.4c1.5.2 2.5 1.2 2.5 3.6H9" fill="#222"/></svg>d.lead@coverdesk.test<svg width="9" height="6" viewBox="0 0 9 6" style="margin-left:4px"><path d="M1 1l3.5 3.5L8 1" fill="none" stroke="#555" stroke-width=".9"/></svg></div>

  <section class="card summary">
    <h2 class="h-card">Today’s Summary</h2>
    <div class="legend">
      <span><i style="background:var(--indigo)"></i>Unfilled</span>
      <span><i style="background:var(--purple-mid)"></i>Filled</span>
      <span><i style="background:var(--purple-light)"></i>No sub needed</span>
      <span><i style="background:var(--blue)"></i>Total</span>
    </div>
    <div class="date">Jan 22</div>
    <div class="stack">
      <span style="width:12px;background:var(--indigo)"></span>
      <span style="width:165px;background:var(--purple-mid)"></span>
      <span style="width:45px;background:var(--purple-light)"></span>
      <span style="flex:1;background:var(--blue)"></span>
    </div>
  </section>

  <section class="card overview">
    <h2>Location Overview</h2>
    <div class="sub">Leave Requests/Openings/Assignments</div>
    <svg class="abs" style="left:0;top:0" width="323" height="220" viewBox="0 0 323 220" font-family="Inter, sans-serif" font-size="5.5" fill="#777">
      <g stroke="#9aa0c8" stroke-width=".5" stroke-dasharray="3 3">
        <line x1="28" y1="59" x2="310" y2="59"/><line x1="28" y1="87.4" x2="310" y2="87.4"/>
        <line x1="28" y1="115.8" x2="310" y2="115.8"/><line x1="28" y1="144.2" x2="310" y2="144.2"/>
        <line x1="28" y1="172.6" x2="310" y2="172.6"/><line x1="28" y1="201" x2="310" y2="201"/>
      </g>
      <line x1="25" y1="59" x2="25" y2="201" stroke="#bbb" stroke-width=".5" stroke-dasharray="1 3"/>
      <text x="15" y="61">10</text><text x="17" y="89">8</text><text x="17" y="118">6</text>
      <text x="17" y="146">4</text><text x="17" y="174">2</text><text x="17" y="203">0</text>
      <g>
        <rect x="46" y="145" width="11" height="56" rx="4" fill="var(--bar-purple)"/>
        <rect x="46" y="145" width="11" height="9" rx="3" fill="var(--bar-green)"/>
        <rect x="93" y="145" width="11" height="56" rx="4" fill="var(--bar-red)"/>
        <rect x="141" y="127" width="11" height="74" rx="4" fill="var(--bar-purple)"/>
        <rect x="190" y="145" width="11" height="56" rx="4" fill="var(--bar-red)"/>
        <rect x="236" y="115" width="11" height="86" rx="4" fill="var(--bar-purple)"/>
        <rect x="281" y="60" width="11" height="141" rx="4" fill="var(--bar-red)"/>
      </g>
      <circle cx="120" cy="208" r="5" fill="var(--teal)"/>
      <circle cx="217" cy="208" r="5" fill="var(--teal)"/>
    </svg>
  </section>

  <section class="card fill">
    <h2>Monthly Fill Rate</h2>
    <svg class="abs" style="left:0;top:0" width="168" height="220" viewBox="0 0 168 220">
      <g transform="rotate(-90 84 117)" fill="none" stroke-width="16">
        <circle cx="84" cy="117" r="28" stroke="var(--indigo)" stroke-dasharray="70.4 175.9"/>
        <circle cx="84" cy="117" r="28" stroke="var(--purple-mid)" stroke-dasharray="58 175.9" stroke-dashoffset="-70.4"/>
        <circle cx="84" cy="117" r="28" stroke="var(--purple-light)" stroke-dasharray="47.5 175.9" stroke-dashoffset="-128.4"/>
      </g>
    </svg>
    <div class="dlabel" style="left:22px;top:68px">No Sub<br>27%</div>
    <div class="dlabel" style="left:122px;top:90px">Filled<br>40 %</div>
    <div class="dlabel" style="left:50px;top:156px">Open<br>33 %</div>
  </section>

  <section class="card profiles">
    <h2 class="h-card">Pending profile images</h2>
  </section>
  <div class="t-small" style="left:874px;top:406px">Profile Images</div>
  <div class="t-small" style="left:687px;top:424px">Last Name</div>
  <div class="t-small" style="left:753px;top:424px">First Name</div>
  <div class="t-small" style="left:846px;top:424px">Pending</div>
  <div class="t-small" style="left:911px;top:424px">Previously Verified</div>
  <div class="t-small" style="left:1009px;top:424px">Option</div>
  <div class="rule" style="left:687px;top:446px;width:357px"></div>

  <div class="t-small" style="left:689px;top:464px">Harlow</div>
  <div class="t-small" style="left:755px;top:464px">Dana</div>
  <div class="photo" role="img" aria-label="Pending profile photo" style="left:850px;top:455px;background:linear-gradient(160deg,#c9b89a,#b07c58)"></div>
  <div class="t-small none" style="left:922px;top:465px">None available</div>
  <div class="rule" style="left:687px;top:489px;width:357px"></div>

  <div class="t-small" style="left:689px;top:504px">Pruitt</div>
  <div class="t-small" style="left:755px;top:504px">Owen</div>
  <div class="photo" role="img" aria-label="Pending profile photo" style="left:850px;top:495px;background:linear-gradient(160deg,#e3ddd6,#9b6c4f)"></div>
  <div class="t-small none" style="left:922px;top:505px">None available</div>
  <div class="rule" style="left:687px;top:529px;width:357px"></div>

  <div class="t-small" style="left:689px;top:545px">Quintero</div>
  <div class="t-small" style="left:755px;top:545px">Lena</div>
  <div class="photo" role="img" aria-label="Pending profile photo" style="left:850px;top:535px;background:linear-gradient(160deg,#8ea48a,#a5765a)"></div>
  <div class="t-small none" style="left:922px;top:546px">None available</div>
  <div class="rule" style="left:680px;top:571px;width:357px"></div>

  <div class="t-small" style="left:689px;top:586px">Whitcombe</div>
  <div class="t-small" style="left:755px;top:586px">Nadia</div>
  <div class="photo" role="img" aria-label="Pending profile photo" style="left:850px;top:577px;background:linear-gradient(160deg,#d7a07e,#c56d6a)"></div>
  <div class="t-small none" style="left:922px;top:587px">None available</div>

  <div class="abs tabs" style="left:189px">Regular Staff Leave Requests</div>
  <div class="abs tabs" style="left:391px">Managed Openings</div>
  <div class="abs tabs" style="left:534px">Leave Requests</div>
  <div class="abs tabs" style="left:659px">Substitute Attendace</div>
  <div class="abs tab-line"></div>

  <section class="card requests"></section>
  <svg class="abs" style="left:160px;top:741px" width="20" height="16" viewBox="0 0 20 16"><rect x=".5" y=".5" width="19" height="15" rx="1.5" fill="#fff" stroke="#333"/><line x1=".5" y1="2.5" x2="19.5" y2="2.5" stroke="#333"/><path d="M10 6v6M7 9h6" stroke="#222" stroke-width=".9"/></svg>
  <div class="col-head big" style="left:223px;top:741px">Status</div>
  <div class="col-head big" style="left:302px;top:741px">Full Name</div>
  <div class="col-head small" style="left:495px;top:730px">Option</div>
  <div class="col-head small" style="left:443px;top:748px">Assigment</div>
  <div class="col-head small" style="left:515px;top:748px">Prearranged Sub</div>
  <div class="col-head big" style="left:633px;top:741px">Time Slots Summary</div>
  <div class="rule" style="left:156px;top:765px;width:656px;background:#c9cde4"></div>

  <svg width="0" height="0" style="position:absolute">
    <defs>
      <symbol id="ico-edit" viewBox="0 0 12 12"><path d="M9 6.5V11H1V3h4.5" fill="none" stroke="#777" stroke-width=".8"/><path d="M4.5 8l.4-1.7L10 1.2l1.2 1.2-5 5z" fill="none" stroke="#777" stroke-width=".8"/></symbol>
      <symbol id="ico-eye" viewBox="0 0 12 8"><path d="M.5 4C2 1.5 4 .5 6 .5s4 1 5.5 3.5C10 6.5 8 7.5 6 7.5S2 6.5.5 4z" fill="none" stroke="#777" stroke-width=".9"/><circle cx="6" cy="4" r="1.8" fill="#777"/></symbol>
    </defs>
  </svg>

  <svg class="abs" style="left:164px;top:773px" width="12" height="12"><use href="#ico-edit"/></svg>
  <svg class="abs" style="left:193px;top:775px" width="12" height="8"><use href="#ico-eye"/></svg>
  <div class="cell" style="left:223px;top:773px">Pending</div>
  <div class="avatar" role="img" aria-label="Staff avatar" style="left:302px;top:774px;background:#b99a86"></div>
  <div class="cell" style="left:317px;top:772px">Ellis Brandt</div>
  <div class="cell" style="left:444px;top:770px">N/A</div>
  <div class="cell" style="left:547px;top:773px">N/A</div>
  <div class="cell" style="left:687px;top:771px">12/22 - 12/22 (0h 30m)</div>
  <div class="rule" style="left:156px;top:792px;width:656px"></div>

  <svg class="abs" style="left:164px;top:799px" width="12" height="12"><use href="#ico-edit"/></svg>
  <svg class="abs" style="left:193px;top:801px" width="12" height="8"><use href="#ico-eye"/></svg>
  <div class="cell" style="left:223px;top:799px">Pending</div>
  <div class="avatar" role="img" aria-label="Staff avatar" style="left:302px;top:800px;background:#9c6b5a"></div>
  <div class="cell" style="left:317px;top:798px">Marcus Keel</div>
  <div class="cell" style="left:444px;top:796px">N/A</div>
  <div class="cell" style="left:547px;top:799px">N/A</div>
  <div class="cell" style="left:687px;top:799px">12/24 - 12/30 (4h 45m)</div>
  <div class="rule" style="left:156px;top:820px;width:656px"></div>

  <svg class="abs" style="left:164px;top:826px" width="12" height="12"><use href="#ico-edit"/></svg>
  <svg class="abs" style="left:193px;top:828px" width="12" height="8"><use href="#ico-eye"/></svg>
  <div class="cell" style="left:223px;top:825px">Pending</div>
  <div class="initials" style="left:301px;top:826px">TF</div>
  <div class="cell" style="left:317px;top:824px">Tessa Fairlie</div>
  <div class="cell" style="left:442px;top:822px">Conselor</div>
  <div class="cell" style="left:687px;top:824px">12/20 - 12/31 (4h 45m)</div>
  <div class="rule" style="left:156px;top:847px;width:656px"></div>

  <svg class="abs" style="left:164px;top:852px" width="12" height="12"><use href="#ico-edit"/></svg>
  <svg class="abs" style="left:193px;top:854px" width="12" height="8"><use href="#ico-eye"/></svg>
  <div class="cell" style="left:223px;top:851px">Pending</div>
  <div class="avatar" role="img" aria-label="Staff avatar" style="left:302px;top:852px;background:#d69a6c"></div>
  <div class="cell" style="left:317px;top:850px">Ruth Okafor</div>
  <div class="cell" style="left:442px;top:848px">N/A</div>
  <div class="cell" style="left:546px;top:851px">N/A</div>
  <div class="cell" style="left:687px;top:853px">12/20 - 01/09 (1h 45m)</div>
  <div class="rule" style="left:156px;top:875px;width:656px"></div>

  <svg class="abs" style="left:164px;top:880px" width="12" height="12"><use href="#ico-edit"/></svg>
  <svg class="abs" style="left:193px;top:882px" width="12" height="8"><use href="#ico-eye"/></svg>
  <div class="cell" style="left:223px;top:879px">Pending</div>
  <div class="avatar" role="img" aria-label="Staff avatar" style="left:302px;top:880px;background:#8a5a46"></div>
  <div class="cell" style="left:317px;top:878px">Gina Holloway</div>
  <div class="cell" style="left:442px;top:876px">Administrator</div>
  <div class="avatar" role="img" aria-label="Staff avatar" style="left:533px;top:881px;background:#b39a84"></div>
  <div class="cell" style="left:547px;top:879px">Paul Denning</div>
  <div class="cell" style="left:687px;top:878px">12/24 - 01/16 (5h 0m)</div>
  <div class="rule" style="left:156px;top:902px;width:656px"></div>

  <svg class="abs" style="left:164px;top:906px" width="12" height="12"><use href="#ico-edit"/></svg>
  <svg class="abs" style="left:193px;top:908px" width="12" height="8"><use href="#ico-eye"/></svg>
  <div class="cell" style="left:223px;top:906px">Pending</div>
  <div class="avatar" role="img" aria-label="Staff avatar" style="left:302px;top:907px;background:#a2705e"></div>
  <div class="cell" style="left:317px;top:905px">Ivy Castellan</div>
  <div class="cell" style="left:442px;top:903px">Administrator</div>
  <div class="cell" style="left:687px;top:908px">12/20 - 01/04 (2h 0m)</div>
  <div class="rule" style="left:156px;top:930px;width:656px"></div>
  <div class="abs scroll"></div>

  <section class="card monthly">
    <h2>Monthly Summary</h2>
  </section>
  <div class="rule" style="left:872px;top:751px;width:173px;background:#c9cde4"></div>
  <div class="stat" style="left:872px;top:764px">Total Jobs</div><div class="stat" style="left:999px;top:764px">45</div>
  <div class="rule" style="left:872px;top:783px;width:173px"></div>
  <div class="stat" style="left:872px;top:791px">Filled Jobs</div><div class="stat" style="left:999px;top:791px">data</div>
  <div class="rule" style="left:872px;top:814px;width:173px"></div>
  <div class="stat" style="left:872px;top:819px">No Sub Jobs</div><div class="stat" style="left:999px;top:819px">data</div>
  <div class="rule" style="left:872px;top:846px;width:173px"></div>

  <div class="btn primary" style="left:855px;top:877px;width:121px">Create Absence</div>
  <div class="btn" style="left:981px;top:877px;width:85px">Approve 8</div>
  <div class="btn" style="left:855px;top:912px;width:121px">Create Vacancy</div>
  <div class="btn" style="left:981px;top:912px;width:85px">Approve 3</div>
</body>
</html>
```